Website for Public Relations Agency called "Bright Lark"

A need a website for a new business which is essentially a Public Relations/ Marketing business. We offer services to small family businesses, medium enterprise as well as multinational companies (ie we sell our professional services to other businesses; we are not a consumer brand).
The website needs to be polished, professional and modern. Because of the services we offer, I really need the website to be a little bit "wow".
Colours - we have a logo (see files) so the colour palette for the website should be dictated by this.
The Word doc attached mapped out the various pages that will make up the site. The text is not 100% finalised but it's good enough to give you a good picture of what the site will talk about.
I am not selling directly off my site, so this is an informational site only to explain who i am and what i do.
Target Market(s)
Other businesses - small family business, medium business and large multinational companies
Industry/Entity Type
Marketing
Coding
Coded - Design and coding required
Number of Pages Required
5+ page
Requirements
Must have
- Given my business, really looking for a little "wow" factor on the home page
Should not have
- I don't know if this is relevant to the coding, but I want to end up on a platform that I can myself make copy/ text edits as I please. I do not want to have to go through a deisgn company for small text changes in 6 or 12 months time.

```html
<!DOCTYPE html>
<html lang="en">
<head>
<meta charset="utf-8">
<title>Bright Lark — Strategic Communication</title>
<link href="https://fonts.googleapis.com/css2?family=Lexend:wght@300;400;500;600&family=Plus+Jakarta+Sans:wght@400;500;600;700&display=swap" rel="stylesheet">
<style>
:root{
  --navy:#2b2661;
  --pink:#e0479a;
  --mauve:#8c72a8;
  --ink:#2b2661;
  --grey:#7d7891;
  --bubble:#f9e6f2;
  --white:#ffffff;
  --muted:#a9a3c8;
}
*{margin:0;padding:0;box-sizing:border-box}
html,body{width:1200px;height:3051px;overflow:hidden}
body{font-family:"Plus Jakarta Sans",sans-serif;color:var(--ink);background:var(--white);position:relative}
h1,h2,h3{font-family:"Lexend",sans-serif;font-weight:400}
a{color:inherit;text-decoration:none}
.btn{position:absolute;display:flex;align-items:center;justify-content:center;font-size:10.5px;font-weight:700;border-radius:4px;color:var(--white)}
.btn--pink{background:var(--pink)}
.btn--mauve{background:var(--mauve)}
.btn--white{background:var(--white);color:var(--ink)}

/* header + hero */
.hero{position:absolute;left:0;top:0;width:1200px;height:550px;background:var(--navy)}
.brand{position:absolute;display:flex;align-items:center;gap:9px}
.brand__dot{width:12px;height:12px;border-radius:50%;background:var(--pink)}
.brand__name{font-family:"Lexend",sans-serif;font-weight:500;color:var(--pink);white-space:nowrap}
.site-head .brand{left:75px;top:28px}
.site-head .brand__name{font-size:30px}
.nav{position:absolute;top:30px;left:630px;display:flex;gap:24px;font-size:10.5px;color:var(--white);font-weight:500}
.nav .is-active{color:var(--pink)}
.nav__phone{position:absolute;left:871px;top:30px;display:flex;align-items:center;gap:7px;font-size:11.5px;color:var(--white)}
.hero__photo{position:absolute;left:381px;top:75px;width:819px;height:550px;background:linear-gradient(120deg,#c9cde0 0%,#dfe3ee 45%,#6aa7e6 62%,#cfd6e6 100%)}
.hero__title{position:absolute;left:75px;top:198px;font-family:"Lexend",sans-serif;font-weight:600;font-size:31px;color:var(--pink);z-index:2}
.hero__sub{position:absolute;left:75px;top:257px;font-size:19.5px;font-weight:700;color:var(--white);z-index:2}
.hero__text{position:absolute;left:75px;top:298px;width:520px;font-size:12px;line-height:19px;color:var(--white);z-index:2}
.hero .btn{left:75px;top:366px;width:125px;height:37px;z-index:2}

/* messaging */
.messaging__art{position:absolute;left:106px;top:625px;width:275px;height:358px;background:linear-gradient(160deg,#d8479a,#7b3563 55%,#c76aa6);border-radius:60px 10px 70px 10px}
.messaging h2{position:absolute;left:470px;top:718px;font-size:30px;line-height:35px;color:var(--ink)}
.messaging h2 em{font-style:normal;color:var(--pink);font-weight:500}
.checklist{position:absolute;left:470px;top:815px;width:560px;list-style:none;font-size:9.5px;font-weight:600;line-height:15px;color:var(--ink)}
.checklist li{position:relative;padding-left:18px;margin-bottom:9px}
.checklist li::before{content:"";position:absolute;left:0;top:7px;width:9px;height:1.3px;background:var(--pink)}
.checklist li::after{content:"";position:absolute;left:5px;top:4.5px;width:4px;height:4px;border-top:1.3px solid var(--pink);border-right:1.3px solid var(--pink);transform:rotate(45deg)}

/* cta */
.cta{position:absolute;left:0;top:1057px;width:1200px;height:345px;background:var(--navy);text-align:center}
.cta__eyebrow{position:absolute;top:76px;width:100%;font-family:"Lexend",sans-serif;font-size:20px;color:var(--pink);font-weight:500}
.cta h2{position:absolute;top:108px;left:200px;width:800px;font-weight:500;font-size:24px;line-height:30px;color:var(--white)}
.cta .btn{left:538px;top:228px;width:124px;height:37px}

/* services */
.services{position:absolute;left:0;top:1402px;width:1200px;height:568px}
.services__photo{position:absolute;inset:0;background:linear-gradient(90deg,#e6579f 0%,#e25d9f 45%,#c678a8 70%,#9a7790 100%)}
.services h2{position:absolute;left:200px;top:73px;font-size:30px;line-height:35px;color:var(--white)}
.services h2 strong{font-weight:600;color:var(--navy)}
.service-list{position:absolute;left:200px;top:170px;width:440px;list-style:none;font-size:12.5px;font-weight:600;line-height:22px;color:var(--white)}
.service-list li{position:relative;padding-left:18px;margin-bottom:3px}
.service-list li::before{content:"";position:absolute;left:0;top:7px;width:8px;height:8px;border-radius:50%;border:1.5px solid var(--navy)}
.services .btn{left:200px;top:456px;width:112px;height:37px}

/* testimonials */
.reviews{position:absolute;left:0;top:1970px;width:1200px;height:573px}
.reviews__mark{position:absolute;left:133px;top:140px;width:14px;height:14px;border-radius:50%;background:var(--pink)}
.reviews h2{position:absolute;left:133px;top:183px;font-size:30px;line-height:35px;color:var(--ink)}
.reviews h2 strong{font-weight:600}
.reviews .btn{left:133px;top:292px;width:124px;height:37px}
.bubble{position:absolute;left:406px;top:75px;width:721px;height:320px;background:var(--bubble);border-radius:24px 24px 24px 0}
.bubble__tail{position:absolute;left:650px;top:394px}
.bubble__quote{position:absolute;left:32px;top:28px;width:660px;font-size:11.3px;line-height:21.3px;color:var(--grey)}
.bubble__quote p{margin-bottom:21px}
.bubble__name{position:absolute;left:32px;top:265px;font-family:"Lexend",sans-serif;font-size:13px;color:var(--ink)}
.bubble__role{position:absolute;left:32px;top:284px;font-size:10.5px;color:var(--grey)}
.carousel-arrow{position:absolute;top:455px}
.avatar{position:absolute;border-radius:50%;background:linear-gradient(135deg,#e9e3ea,#cfc6cf)}

/* footer */
.site-foot{position:absolute;left:0;top:2543px;width:1200px;height:508px;background:var(--navy)}
.acknowledge{position:absolute;left:220px;top:54px;width:760px;text-align:center;font-size:11px;line-height:21px;color:var(--muted)}
.rule{position:absolute;left:200px;width:800px;height:1px;background:rgba(255,255,255,.1)}
.site-foot .brand{left:200px;top:246px}
.site-foot .brand__name{font-size:36px}
.foot-col h3{position:absolute;font-family:"Plus Jakarta Sans",sans-serif;font-weight:700;font-size:13px;color:var(--white)}
.contact-line{position:absolute;left:492px;display:flex;align-items:center;gap:8px;font-size:12.5px;color:var(--muted)}
.social{position:absolute;left:290px;top:347px;width:38px;height:38px;border-radius:50%;border:1px solid rgba(255,255,255,.35)}
.site-foot .btn{left:492px;top:350px;width:113px;height:37px}
.newsletter{position:absolute;left:781px;top:285px;width:200px;font-size:11.5px;line-height:17px;color:var(--muted)}
.email-field{position:absolute;left:781px;top:350px;width:219px;height:37px;background:#3a3573;border-radius:4px;display:flex;align-items:center;justify-content:space-between;padding:0 12px;font-size:9px;color:#d9d5ea}
.copyright{position:absolute;left:200px;top:467px;font-size:9.5px;color:var(--muted)}
.copyright span{color:var(--pink)}
.foot-nav{position:absolute;left:492px;top:467px;display:flex;gap:14px;font-size:9.5px;color:var(--muted)}
.foot-nav .is-active{color:var(--pink)}
.to-top{position:absolute;left:1117px;top:462px}
</style>
</head>
<body>

<header class="hero site-head">
  <a class="brand" href="#"><span class="brand__dot"></span><span class="brand__name">Bright Lark</span></a>
  <nav class="nav">
    <a class="is-active" href="#">Home</a><a href="#">About</a><a href="#">How we help</a><a href="#">Fees</a>
  </nav>
  <div class="nav__phone">
    <svg width="13" height="13" viewBox="0 0 24 24" fill="none" stroke="#fff" stroke-width="2"><path d="M5 3h4l2 5-3 2a12 12 0 0 0 6 6l2-3 5 2v4a2 2 0 0 1-2 2A18 18 0 0 1 3 5a2 2 0 0 1 2-2z"/></svg>
    +61 400 555 019
  </div>
  <a class="btn btn--pink" href="#" style="left:1013px;top:19px;width:112px;height:37px">Get in touch</a>

  <div class="hero__photo" role="img" aria-label="Portrait of the founder in a blue blazer, resting her chin on her hand"></div>
  <h1 class="hero__title">Carefully Considered. Expertly Crafted.</h1>
  <p class="hero__sub">Strategic Communication &amp; Reputation Management Specialist</p>
  <p class="hero__text">When you have a message to deliver, a story to tell, something to say that you need your stakeholders to hear loud and clear... Bright Lark can help.</p>
  <a class="btn btn--mauve" href="#">Contact us today!</a>
</header>

<section class="messaging">
  <div class="messaging__art" role="img" aria-label="Collage of team photos in a bold pink frame"></div>
  <h2>In Business, <em>Messaging<br>Always Matters</em></h2>
  <ul class="checklist">
    <li>Do you have a message to share that will build trust with the audiences that drive your revenue?</li>
    <li>Perhaps you need help promoting your people or services, or ensure they are known by a wider audience?</li>
    <li>Is there a narrative to be carefully devised and managed to prevent the erosion of trust amongst your<br>important stakeholders, either internal or external?</li>
    <li>Do you have a situation on your hands, and you feel like you need to go into damage control?</li>
    <li>Has the media come knocking and you're not sure what to say?</li>
    <li>Do you need a website that is cohesive and sharp?</li>
  </ul>
</section>

<section class="cta">
  <p class="cta__eyebrow">Get in touch</p>
  <h2>We'd love to talk about how we can help shape your narrative,<br>overcome your communications challenges, and<br>support you to say what needs to be said.</h2>
  <a class="btn btn--pink" href="#">Contact us today!</a>
</section>

<section class="services">
  <div class="services__photo" role="img" aria-label="Team of colleagues working together around a laptop, tinted pink"></div>
  <h2>We Help You <strong>Communicate with<br>Clarity &amp; Impact</strong></h2>
  <ul class="service-list">
    <li>Media Strategy, Liaison, Management And Execution</li>
    <li>Crisis, Issues &amp; Reputation Management (Specialising In Post Cyber Incident Communications)</li>
    <li>Corporate Communication</li>
    <li>Executive &amp; Internal Communication</li>
    <li>Communications Strategy &amp; Counsel</li>
    <li>B2B Public Relations</li>
    <li>Brand Building</li>
    <li>Copyrighting (In All Its Forms)</li>
    <li>Narrative Development</li>
    <li>Change Communications</li>
  </ul>
  <a class="btn btn--white" href="#">Get in touch</a>
</section>

<section class="reviews">
  <span class="reviews__mark"></span>
  <h2>Our clients<br><strong>say this</strong></h2>
  <a class="btn btn--mauve" href="#">Contact us today!</a>

  <div class="bubble">
    <div class="bubble__quote">
      <p>"We engaged Ella Morrow of Bright Lark to assist with an announcement about leadership changes and growth ambitions. crafting the right message for our market was a challenge; strategically we were hoping for some industry media coverage. Ella did what Ella said she would and successfully secured this coverage to meet our objectives.</p>
      <p>Ella made the entire process quick and seamless. she took the time to ask insightful questions to truly understand the message we wanted to convey. the end result was exactly what we needed. our press release was picked up by the targeted publications, and the response from the market was overwhelmingly positive.</p>
      <p>We are extremely impressed with Ella's media counsel and highly recommend Bright Lark to anyone in need of professional, impactful media relations services and or/ great copywriting."</p>
    </div>
    <p class="bubble__name">Daniel Hart</p>
    <p class="bubble__role">Harbour Underwriting</p>
  </div>
  <svg class="bubble__tail" width="66" height="24" viewBox="0 0 66 24"><path d="M0 0H66L60 24Z" fill="var(--bubble)"/></svg>

  <svg class="carousel-arrow" style="left:458px" width="26" height="10" viewBox="0 0 26 10" fill="none" stroke="#e0479a" stroke-width="1.3"><path d="M25 5H1M6 1L1 5l5 4"/></svg>
  <div class="avatar" style="left:503px;top:435px;width:50px;height:50px" role="img" aria-label="Client portrait"></div>
  <div class="avatar" style="left:616px;top:435px;width:50px;height:50px" role="img" aria-label="Client portrait"></div>
  <div class="avatar" style="left:728px;top:422px;width:76px;height:76px;background:linear-gradient(135deg,#c9bfc2,#6b5a55)" role="img" aria-label="Portrait of the featured client"></div>
  <div class="avatar" style="left:866px;top:435px;width:50px;height:50px" role="img" aria-label="Client portrait"></div>
  <div class="avatar" style="left:978px;top:435px;width:50px;height:50px" role="img" aria-label="Client portrait"></div>
  <svg class="carousel-arrow" style="left:1050px" width="26" height="10" viewBox="0 0 26 10" fill="none" stroke="#e0479a" stroke-width="1.3"><path d="M1 5h24M20 1l5 4-5 4"/></svg>
</section>

<footer class="site-foot">
  <p class="acknowledge">Bright Lark acknowledges the traditional owners of country throughout the land we call australia. in particular, we pay our respect to the cameraygal people of the eora nation whose country our business operates from. indeed, we recognise all first nations peoples' continuing connection to land, waters and culture and pay our respects to their elders past and present</p>
  <div class="rule" style="top:164px"></div>

  <a class="brand" href="#"><span class="brand__dot"></span><span class="brand__name">Bright Lark</span></a>
  <span class="social" aria-label="Social profile"></span>

  <div class="foot-col">
    <h3 style="left:492px;top:249px">Contact Us</h3>
    <div class="contact-line" style="top:285px">
      <svg width="11" height="11" viewBox="0 0 24 24" fill="none" stroke="#e0479a" stroke-width="2.4"><path d="M5 3h4l2 5-3 2a12 12 0 0 0 6 6l2-3 5 2v4a2 2 0 0 1-2 2A18 18 0 0 1 3 5a2 2 0 0 1 2-2z"/></svg>
      +61 400 555 019
    </div>
    <div class="contact-line" style="top:315px">
      <svg width="11" height="11" viewBox="0 0 24 24" fill="#e0479a"><path d="M2 9l10 6 10-6v11H2z"/><path d="M2 7l10-5 10 5-10 6z"/></svg>
      ella.morrow@brightlark.com.au
    </div>
    <a class="btn btn--pink" href="#">Get in touch</a>
  </div>

  <div class="foot-col">
    <h3 style="left:781px;top:249px">Stay Connected</h3>
    <p class="newsletter">Sign up for newsletter to receive Upadates, tips, and exclusive content.</p>
    <div class="email-field">Enter your email...
      <svg width="11" height="11" viewBox="0 0 24 24" fill="#e0479a"><path d="M2 3l20 9-20 9 4-9z"/></svg>
    </div>
  </div>

  <div class="rule" style="top:436px"></div>
  <p class="copyright">© 2024 <span>Bright Lark</span>. All Rights Reserved</p>
  <nav class="foot-nav"><a class="is-active" href="#">Home</a><span>|</span><a href="#">About</a><span>|</span><a href="#">How we help</a><span>|</span><a href="#">Fees</a></nav>
  <svg class="to-top" width="16" height="18" viewBox="0 0 16 18"><path d="M8 0L16 18 8 13 0 18Z" fill="#e0479a"/></svg>
</footer>

</body>
</html>
```